The Brightwater Compass Business Card

We need an attractive business card with the logo that we bought from ArtVantly last year.
Our mission is to contribute to change the way today's leaders manage business companies bringing value to the workplace and helping them to build a new model of creating wealth.
Our logo is clear about our values : we seek Positive Change through People and are convinced that the pursuit of individual well-being and the chase of economic results can converge with the right management.
Management Consulting
Corinne Fabrelle
+34 612 98 70 31
corinne.fabrelle@thebrightwatercompass-mail.net
www.thebrightwatercompass-mail.net

```html
<!DOCTYPE html>
<html lang="en">
<head>
<meta charset="utf-8">
<title>The Brightwater Compass Business Card</title>
<link rel="stylesheet" href="https://fonts.googleapis.com/css2?family=Arimo:wght@400;700&family=Cinzel:wght@500&display=swap">
<style>
  :root {
    --teal: #0f7f78;
    --teal-deep: #0b6661;
    --teal-soft: #d3e6e4;
    --ink: #1b1b1b;
    --paper: #ffffff;
    --backdrop: #2a2a2a;
    --band-dark: #151515;
  }
  * { box-sizing: border-box; margin: 0; padding: 0; }
  html, body { width: 1200px; height: 997px; overflow: hidden; }
  body {
    background: var(--backdrop);
    font-family: "Arimo", Arial, sans-serif;
    position: relative;
  }
  .card {
    position: absolute;
    left: 250px;
    width: 700px;
    height: 400px;
    border-radius: 22px;
    overflow: hidden;
  }
  .card-back { top: 68px; background: var(--teal); }
  .card-front { top: 528px; background: var(--paper); }

  .wordmark {
    position: absolute;
    display: flex;
    align-items: center;
    gap: 14px;
    font-family: "Cinzel", Georgia, serif;
    font-weight: 500;
    letter-spacing: 1px;
    white-space: nowrap;
  }
  .wordmark .dot { width: 18px; height: 18px; border-radius: 50%; }
  .card-back .wordmark {
    left: 50%; top: 50%; transform: translate(-50%, -50%);
    color: var(--paper); font-size: 36px;
  }
  .card-back .wordmark .dot { background: var(--paper); }
  .card-front .wordmark {
    left: 44px; top: 92px; color: var(--teal-deep); font-size: 30px;
  }
  .card-front .wordmark .dot { background: var(--teal-deep); }

  .leaf-motif {
    position: absolute; right: -40px; top: -20px;
    width: 430px; height: 400px;
    background: radial-gradient(ellipse at 55% 45%, var(--teal-soft) 0%, rgba(211,230,228,0.5) 55%, rgba(255,255,255,0) 75%);
  }

  .holder { position: absolute; right: 34px; top: 132px; text-align: right; }
  .holder-name { color: var(--teal); font-weight: 700; font-size: 24px; }
  .holder-role { color: var(--ink); font-weight: 700; font-size: 14px; margin-top: 4px; letter-spacing: 0.5px; }

  .rule { position: absolute; left: 44px; top: 234px; width: 560px; height: 2px; background: var(--teal); }

  .contacts { position: absolute; left: 44px; bottom: 40px; list-style: none; }
  .contacts li {
    display: flex; align-items: center; gap: 10px;
    font-size: 16px; color: var(--ink); margin-top: 8px;
  }
  .contacts svg { width: 20px; height: 20px; flex: none; }

  .web-band {
    position: absolute; right: 0; bottom: 58px;
    width: 330px; height: 40px;
    background: var(--teal);
    clip-path: polygon(16px 0, 100% 0, 100% 100%, 0 100%);
    color: var(--paper); font-size: 15px;
    display: flex; align-items: center; justify-content: flex-end; padding-right: 22px;
  }
  .base-band {
    position: absolute; left: 0; right: 0; bottom: 0; height: 58px;
    background: linear-gradient(90deg, var(--paper) 0%, var(--paper) 50%, var(--band-dark) 50%, var(--band-dark) 100%);
    clip-path: polygon(52% 0, 100% 0, 100% 100%, 0 100%, 0 100%);
    opacity: 0;
  }
  .dark-strip {
    position: absolute; right: 318px; bottom: 58px;
    width: 70px; height: 40px; background: var(--band-dark);
    clip-path: polygon(54px 0, 70px 0, 54px 100%, 0 100%);
  }
</style>
</head>
<body>
  <section class="card card-back" aria-label="Card back">
    <div class="wordmark"><span class="dot"></span>The Brightwater Compass</div>
  </section>

  <section class="card card-front" aria-label="Card front">
    <div class="leaf-motif" role="img" aria-label="Faint leafy tree decoration"></div>
    <div class="wordmark"><span class="dot"></span>The Brightwater Compass</div>
    <div class="holder">
      <p class="holder-name">Corinne Fabrelle</p>
      <p class="holder-role">FOUNDER</p>
    </div>
    <div class="rule"></div>
    <ul class="contacts">
      <li>
        <svg viewBox="0 0 20 20" aria-hidden="true"><circle cx="10" cy="10" r="10" fill="var(--teal)"/><path d="M6.5 5.5l2 0 1 2.5-1.3 1a6 6 0 0 0 2.8 2.8l1-1.3 2.5 1v2a1 1 0 0 1-1 1A8 8 0 0 1 5.5 6.5a1 1 0 0 1 1-1z" fill="#fff"/></svg>
        +34 612 98 70 31
      </li>
      <li>
        <svg viewBox="0 0 20 20" aria-hidden="true"><circle cx="10" cy="10" r="10" fill="var(--teal)"/><rect x="5" y="6.5" width="10" height="7" rx="1" fill="#fff"/><path d="M5.5 7l4.5 3.5L14.5 7" stroke="var(--teal)" stroke-width="1" fill="none"/></svg>
        corinne.fabrelle@thebrightwatercompass-mail.net
      </li>
    </ul>
    <div class="dark-strip"></div>
    <div class="web-band">www.thebrightwatercompass-mail.net</div>
  </section>
</body>
</html>
```